Business Card Design for a Personal Trainer

I need a business card design for my job as a personal trainer. It should have a unique, modern and exclusive design. On the front there should be only my logo with my name and my job. 0163/2918374 Tobias Kellinger Lindenfeldweg 14 80412 Munich Germany The most important contact information is the web adress. it can be bigger than the rest, but its not necessary. The card should be 8,5cmx5,5cm big. Font: Roboto. Colors: black, white, gray, 56c1ff.

```html
<!DOCTYPE html>
<html lang="de">
<head>
<meta charset="utf-8">
<title>Tobias Kellinger – Personal Trainer Business Card</title>
<link href="https://fonts.googleapis.com/css2?family=Roboto:wght@300;400&family=Roboto+Condensed:wght@500;700&display=swap" rel="stylesheet">
<style>
  :root {
    --backdrop: #5b5b5b;
    --card: #3b3b3b;
    --white: #ffffff;
    --rule: #cfcfcf;
    --photo-light: #8a8a8a;
    --photo-dark: #2a2a2a;
  }
  * { margin: 0; padding: 0; box-sizing: border-box; }
  html, body {
    width: 1200px; height: 1200px; overflow: hidden;
    background: var(--backdrop);
    font-family: "Roboto", sans-serif;
    color: var(--white);
  }
  .card {
    position: absolute;
    top: 196px;
    width: 464px; height: 810px;
    background: var(--card);
    box-shadow: 0 30px 50px rgba(0,0,0,.45);
    overflow: hidden;
  }
  .card--front { left: 77px; }
  .card--back { left: 658px; }

  .brand {
    position: absolute; top: 120px; left: 0; width: 100%;
    text-align: center;
  }
  .brand__square {
    width: 40px; height: 40px; margin: 0 auto 38px;
    background: var(--white);
  }
  .brand__name {
    font-weight: 300; font-size: 35px; letter-spacing: .5px;
    text-transform: uppercase; line-height: 1;
  }
  .brand__role {
    display: flex; align-items: center; justify-content: center; gap: 8px;
    margin-top: 6px;
    font-weight: 400; font-size: 13px; letter-spacing: 3.6px;
    text-transform: uppercase;
  }
  .brand__role::before, .brand__role::after {
    content: ""; width: 56px; height: 1px; background: var(--white);
  }

  .contact {
    position: absolute; left: 67px; top: 522px;
    list-style: none;
    font-weight: 300; font-size: 21px; letter-spacing: .8px;
  }
  .contact__item {
    padding: 4px 0 6px;
    border-bottom: 1px solid var(--rule);
    line-height: 28px;
  }
  .contact__item--phone { width: 182px; }
  .contact__item--mail { width: 337px; }
  .contact__item--web { width: 289px; }
  .contact__item--address { width: 245px; }
  .contact__marker {
    width: 22px; height: 5px; margin-top: -3px;
    background: var(--white);
  }

  .portrait {
    position: absolute; left: 0; top: 34px;
    width: 306px; height: 776px;
    background: radial-gradient(ellipse at 45% 25%, var(--photo-light), var(--photo-dark) 70%);
  }
  .identity {
    position: absolute; right: 30px; top: 170px;
    text-align: right;
  }
  .identity__name {
    font-family: "Roboto Condensed", sans-serif;
    font-weight: 500; font-size: 38px; line-height: 1;
    text-transform: uppercase; letter-spacing: -.3px;
  }
  .identity__title {
    margin-top: 6px;
    font-weight: 400; font-size: 22px; letter-spacing: .8px;
    text-transform: uppercase;
  }
</style>
</head>
<body>
  <section class="card card--front">
    <div class="brand">
      <div class="brand__square"></div>
      <h1 class="brand__name">Tobias Kellinger</h1>
      <p class="brand__role">Personal Trainer</p>
    </div>
    <ul class="contact">
      <li class="contact__item contact__item--phone">+0163/2918374</li>
      <li class="contact__item contact__item--mail">training@tobiaskellinger.de</li>
      <li class="contact__item contact__item--web">www.tobiaskellinger.de</li>
      <li class="contact__item contact__item--address">Lindenfeldweg 14<br>80412 München</li>
      <li class="contact__marker"></li>
    </ul>
  </section>

  <section class="card card--back">
    <div class="portrait" role="img" aria-label="Black and white portrait of the trainer with arms crossed, wearing a dark athletic shirt"></div>
    <div class="identity">
      <h2 class="identity__name">Tobias Kellinger</h2>
      <p class="identity__title">Manager</p>
    </div>
  </section>
</body>
</html>
```